Eye Grabbing - Travel Consultant Business Card

I need a business card that stands out. Vertical instead of horizontal, rounded edges, would love to use the same layout item for magnets. I have uploaded my current logo and tag line. Would love a cool eye-grabbing image for the front side. Can be something different than what you see on my website as I am looking to rebrand as a Leisure, Luxury & Adventure Specialist.

Target Market(s)

Leisure and Luxury Travel

Industry/Entity Type

Travel Agent

Contact Information for Business Card

Company Name - uMbrela Travel; Name - Rhoda Peverell; Title - Travel Consultant; Website - www.umbrelatravel.example ; Phone: 318-662-0951 Email rhoda@umbrelatravel.example and my facebook, twitter, and Instagram handles

Font styles to use
Serif

Colors

Designer to choose colors to be used in the design.

Requirements
Must have
• my tag line of -- Dream Explore Discover
Nice to have

```html
<!DOCTYPE html>
<html lang="en">
<head>
<meta charset="utf-8">
<title>uMbrela Travel — Business Card</title>
<link rel="stylesheet" href="https://fonts.googleapis.com/css2?family=Lora:wght@400;600;700&family=Playfair+Display:wght@700&display=swap">
<style>
  :root {
    --stage: #2b2624;
    --card: #0b0b0c;
    --card-edge: #1d1d1f;
    --rule: #3a3a3c;
    --ink: #e9ecef;
    --ink-soft: #b9c0c7;
    --aqua: #3cc6d6;
    --sky: #5fb8e8;
    --lime: #c9e32f;
    --green: #3fbf5a;
    --blue: #2f6fd0;
    --dusk-1: #0f3b57;
    --dusk-2: #1f8a9c;
    --dusk-3: #e3a44a;
    --icon-fb: #3b5a9a;
    --icon-tw: #2aa3e8;
    --icon-ig: #4b7fa6;
  }
  * { box-sizing: border-box; margin: 0; padding: 0; }
  html, body { width: 1200px; height: 844px; overflow: hidden; background: var(--stage); }
  .canvas {
    width: 1200px; height: 844px;
    display: flex; align-items: center; justify-content: center; gap: 60px;
  }
  .card {
    position: relative; width: 380px; height: 640px;
    background: var(--card); border: 1px solid var(--card-edge); border-radius: 22px;
    overflow: hidden; font-family: "Lora", serif; color: var(--ink);
  }

  /* Front: image and tagline */
  .hero {
    position: absolute; left: 0; top: 0; width: 100%; height: 430px;
    background: linear-gradient(180deg, var(--dusk-1) 0%, var(--dusk-2) 55%, var(--dusk-3) 100%);
  }
  .hero-fade {
    position: absolute; left: 0; top: 330px; width: 100%; height: 100px;
    background: linear-gradient(180deg, rgba(11,11,12,0) 0%, var(--card) 100%);
  }
  .front-body {
    position: absolute; left: 0; right: 0; top: 450px;
    display: flex; flex-direction: column; align-items: center; gap: 16px;
  }
  .emblem { width: 40px; height: 40px; border-radius: 50%; background: var(--aqua); }
  .front-name { font-weight: 700; font-size: 26px; color: var(--aqua); }
  .tagline {
    font-size: 18px; letter-spacing: 3px; font-style: italic;
    background: linear-gradient(90deg, var(--lime), var(--green) 50%, var(--blue));
    -webkit-background-clip: text; background-clip: text; color: transparent;
  }

  /* Back: contact */
  .brand {
    position: absolute; left: 0; right: 0; top: 70px;
    display: flex; flex-direction: column; align-items: center; gap: 18px;
  }
  .brand-dot { width: 72px; height: 72px; border-radius: 50%; background: var(--aqua); }
  .brand-name { font-weight: 700; font-size: 32px; color: var(--aqua); }
  .divider { position: absolute; left: 50px; right: 50px; height: 1px; background: var(--rule); }
  .divider.top { top: 270px; }
  .divider.bottom { top: 540px; }
  .details { position: absolute; left: 50px; right: 40px; top: 300px; }
  .person {
    font-family: "Playfair Display", serif; font-weight: 700; font-size: 24px;
    color: var(--sky); text-transform: uppercase; letter-spacing: 1px;
  }
  .role { font-size: 15px; font-style: italic; color: var(--ink-soft); margin-top: 4px; }
  .contact { list-style: none; margin-top: 26px; font-size: 15px; line-height: 30px; color: var(--ink); }
  .contact li { display: flex; align-items: center; gap: 10px; white-space: nowrap; }
  .contact svg { width: 13px; height: 13px; flex: none; fill: var(--ink-soft); }
  .social { position: absolute; left: 0; right: 0; top: 566px; display: flex; justify-content: center; gap: 12px; }
  .social span { width: 30px; height: 30px; border-radius: 50%; }
  .social .fb { background: var(--icon-fb); }
  .social .tw { background: var(--icon-tw); }
  .social .ig { background: var(--icon-ig); }
</style>
</head>
<body>
<main class="canvas">
  <section class="card card-front">
    <div class="hero" role="img" aria-label="Eye-catching travel photograph: luxury resort coastline at dusk"></div>
    <div class="hero-fade"></div>
    <div class="front-body">
      <span class="emblem"></span>
      <span class="front-name">uMbrela Travel</span>
      <p class="tagline">Dream. Explore. Discover</p>
    </div>
  </section>

  <section class="card card-contact">
    <div class="brand">
      <span class="brand-dot"></span>
      <span class="brand-name">uMbrela Travel</span>
    </div>
    <div class="divider top"></div>
    <div class="details">
      <h1 class="person">Rhoda Peverell</h1>
      <p class="role">Travel Consultant</p>
      <ul class="contact">
        <li><svg viewBox="0 0 12 12"><path d="M2 1h3l1 3-1.5 1a7 7 0 0 0 3 3L8.5 6.5l3 1v3a1 1 0 0 1-1 1A10 10 0 0 1 .5 2a1 1 0 0 1 1.5-1z"/></svg>318-662-0951</li>
        <li><svg viewBox="0 0 12 12"><path d="M0 2h12v8H0z M0 2l6 4 6-4" stroke="#0b0b0c" stroke-width="1"/></svg>rhoda@umbrelatravel.example</li>
        <li><svg viewBox="0 0 12 12"><circle cx="6" cy="6" r="5.5"/></svg>www.umbrelatravel.example</li>
      </ul>
    </div>
    <div class="divider bottom"></div>
    <div class="social" aria-label="Social profiles">
      <span class="fb"></span><span class="tw"></span><span class="ig"></span>
    </div>
  </section>
</main>
</body>
</html>
```